Web re-design project www.varvikworks.com

We need a corporate website for a startup company called Varvik Works. The company offers web-based worksite management system for big construction companies. In short, replacing annoying papers with iPads.
We need the site main page to provide basic overview of the company and then inner page layout for displaying news and detailed information about products.
Currently we have a site up at:
http://www.varvikworks.com/en/main
but as you can see the graphic design is a bit lacking in quality(implemented by a tech guy :)
We need you to pimp that web site design up!
There is possibility for more freelance work in the future related to our web products, slide show designs and printed marketing materials.
Our main product is PELMO. You can find a short presentation about what it does here:
http://www.varvikworks.com/en/pelmo
Here you can find packages of images and screenshots related to our company:
https://files.stashbin.example/u/7720419/varvik_images.zip
https://files.stashbin.example/u/7720419/varvikworks%20images2.zip
Product logo svg can be found here:
https://files.stashbin.example/u/7720419/PELMO-logo.svg
Your are not forced to use those images, but hopefully there will be something that is useful.
Hope to hear from you guys soon!
Cheers,
Aarni
Update:
We will be using PELMO logo as the company brand. I don't like our current Varvik Works company logo, so that doesn't need to be included in the site design.
Update 2:
I like website designs that are "light", elegant and pretty simplistic. One example is our product login page (screenshot included in files).
Update 3:
Sites from the same industry / type of products:
http://www.rakomesta.fi/
http://www.brellinsurvey.com/products/software/network-applications/gradelane-3d
http://www.quostar.com/construction/heavy-civil/software-solutions/Linked-Crewfield.aspx?dtID=overview&
Target Market(s)
Target audience for the website is companies in the construction sector, and possibly corporate investors
Industry/Entity Type
Graphic Design
Look and feel

```html
<!DOCTYPE html>
<html lang="en">
<head>
<meta charset="utf-8">
<title>Varvik Works</title>
<link rel="stylesheet" href="https://fonts.googleapis.com/css2?family=Ubuntu:wght@500;700&family=Arimo:wght@400;700&display=swap">
<style>
:root{
  --ink:#111;
  --muted:#777;
  --nav-top:#3a3a3a;
  --nav-bottom:#0a0a0a;
  --blue:#29a8e0;
  --blue-light:#4cc0f0;
  --blue-dark:#1a94cf;
  --link:#1ea6df;
  --rule:#cfcfcf;
  --page:#ffffff;
}
*{margin:0;padding:0;box-sizing:border-box}
html,body{width:1200px;height:1050px;overflow:hidden;background:var(--page)}
body{font-family:"Arimo",Arial,sans-serif;color:var(--ink);position:relative}
.site-header{height:108px;background:linear-gradient(#fff,#f0f0f0);position:relative}
.brand{position:absolute;left:124px;top:28px;font-family:"Ubuntu",sans-serif;font-weight:500;font-size:32px;color:#222;display:flex;align-items:center;gap:10px;letter-spacing:1px}
.brand-mark{width:14px;height:14px;border-radius:50%;background:#222}
.call{position:absolute;right:122px;top:24px;font-family:"Ubuntu",sans-serif;font-weight:700;font-size:18px;color:#444;letter-spacing:.5px}
.social{position:absolute;right:122px;top:62px;display:flex;gap:6px}
.social span{width:28px;height:28px;border-radius:4px;background:linear-gradient(#f2f2f2,#d8d8d8);border:1px solid #c4c4c4}
.main-nav{height:41px;background:linear-gradient(var(--nav-top),var(--nav-bottom));border-top:3px solid #222;display:flex;padding-left:131px;gap:0}
.main-nav a{font-family:"Ubuntu",sans-serif;font-weight:700;font-size:14px;color:#fff;text-decoration:none;line-height:36px;letter-spacing:.5px}
.main-nav a:nth-child(1){margin-right:51px}
.main-nav a:nth-child(2){margin-right:51px}
.main-nav a:nth-child(3){margin-right:51px}
.hero{position:absolute;top:149px;left:0;width:1200px;height:497px;background:linear-gradient(100deg,#6b6058 0%,#7a6f66 25%,#4c5036 45%,#8a8580 70%,#6a625c 100%)}
.hero-dots{position:absolute;left:559px;top:460px;display:flex;gap:5px}
.hero-dots span{width:13px;height:13px;border-radius:50%;background:#d9d9d9;border:1px solid #999}
.hero-dots span.active{background:var(--blue)}
.cards{position:absolute;top:671px;left:120px;display:flex;gap:30px}
.card{width:300px;height:280px;border:1px solid #e4e4e4;background:#fff;box-shadow:0 0 12px rgba(0,0,0,.06)}
.card-title{height:32px;background:linear-gradient(var(--blue-light),var(--blue-dark));color:#fff;font-family:"Ubuntu",sans-serif;font-weight:500;font-size:15px;line-height:32px;padding-left:18px;letter-spacing:.8px}
.card-photo{margin:12px 0 0 9px;width:279px;height:119px;border:3px solid #d8d8d8}
.photo-a{background:linear-gradient(90deg,#3a2620,#6a4030 40%,#3c3020)}
.photo-b{background:linear-gradient(90deg,#2f4f8a,#b89a40 40%,#e46a20 60%,#3a5a40)}
.card-lead{font-weight:700;font-size:12px;margin:19px 0 0 8px}
.card-body{font-size:11.5px;line-height:14.5px;margin:16px 4px 0 8px}
.card-body .fade{color:#ddd}
.news-item{margin:0 8px 0 6px;padding:9px 0 6px;border-bottom:1px solid #bbb}
.news-item:last-child{border-bottom:none}
.news-item h3{font-size:14px;font-weight:700;color:var(--link)}
.news-item p{font-size:11.5px;line-height:14.5px}
.news-meta{display:flex;justify-content:space-between;font-weight:700;font-size:12.5px;margin-top:2px;padding-right:6px}
.news-meta span:last-child{font-size:12px}
.site-footer{position:absolute;top:981px;left:120px;width:960px;border-top:1px solid #ddd;display:flex;justify-content:space-between;padding:18px 2px 0 10px;font-size:12px;color:var(--muted)}
</style>
</head>
<body>
<header class="site-header">
  <div class="brand"><span class="brand-mark"></span>Varvik Works</div>
  <div class="call">CALL US : +358 40 712 5530</div>
  <div class="social" aria-label="Social links"><span></span><span></span><span></span><span></span></div>
</header>
<nav class="main-nav">
  <a href="#">HOME</a><a href="#">PRODUCTS</a><a href="#">NEWS</a><a href="#">CONTACT</a>
</nav>
<section class="hero" role="img" aria-label="Site worker in hard hat and hi-vis jacket using a tablet on a gravel worksite">
  <div class="hero-dots"><span class="active"></span><span></span><span></span><span></span><span></span></div>
</section>
<main class="cards">
  <article class="card">
    <h2 class="card-title">WHAT WE DO ?</h2>
    <div class="card-photo photo-a" role="img" aria-label="Worker in hard hat reading closely"></div>
    <p class="card-lead">Sed ut perspiciatis unde omnis iste natus error sit</p>
    <p class="card-body">voluptatem accusantium doloremque laudantiu itotam rem aperiam, eaque ipsa quae ab illo inventorvertatis et quasi architecto beatae vitae dicta sxplicabo. Nemo enim ipsam voluptatem quia voluptas <span class="fade">sit aut fugit sed quia consequuntur mag</span></p>
  </article>
  <article class="card">
    <h2 class="card-title">PROJECTS</h2>
    <div class="card-photo photo-b" role="img" aria-label="Operator in orange vest inside an excavator cab"></div>
    <p class="card-lead">Sed ut perspiciatis unde omnis iste natus error sit</p>
    <p class="card-body">voluptatem accusantium doloremque laudantiu itotam rem aperiam, eaque ipsa quae ab illo inventorvertatis et quasi architecto beatae vitae dicta sxplicabo. Nemo enim ipsam voluptatem quia voluptas <span class="fade">sit aut fugit sed quia consequuntur mag</span></p>
  </article>
  <article class="card">
    <h2 class="card-title">LATEST NEWS</h2>
    <div class="news-item"><h3>Welcome to our new website!</h3><p>Varvik Works new website has been launched. From these pages you can find information about PELMO...</p><div class="news-meta"><span>25.10.2012:</span><span>READ MORE»</span></div></div>
    <div class="news-item"><h3>Welcome to our new website!</h3><p>Varvik Works new website has been launched. From these pages you can find information about PELMO...</p><div class="news-meta"><span>25.10.2012:</span><span>READ MORE»</span></div></div>
    <div class="news-item"><h3>Welcome to our new website!</h3><p>Varvik Works new website has been launched. From these pages you can find information about PELMO...</p><div class="news-meta"><span>25.10.2012:</span><span>READ MORE»</span></div></div>
  </article>
</main>
<footer class="site-footer">
  <span>© 2012 varvikworks. All rights reserved.</span>
  <span>Privacy Policy | T&amp;C</span>
</footer>
</body>
</html>
```